Halvex Consulting

Hi,
I have my own network consulting business (just me)
and need to get a logo and business card design together,

Based in New Zealand,

Gareth Pollard
Unified Communications and Network Architect

/design engineer,
and would like this to be the basis for personal branding and company identity

Reason: I will be off site for a couple of days - so you have some more time

Business

• I have the basis for a optional logo - needs color -

```html
<!DOCTYPE html>
<html lang="en">
<head>
<meta charset="utf-8">
<title>Halvex Consulting – Business Card</title>
<link href="https://fonts.googleapis.com/css2?family=Questrial&display=swap" rel="stylesheet">
<style>
  :root {
    --brand-blue: #1f7fc8;
    --brand-blue-dark: #1a6fb3;
    --pattern-light: #4c95d3;
    --card-white: #ffffff;
    --card-grey: #eeeeee;
    --ink: #222222;
    --stage: #e9e9e9;
  }
  * { margin: 0; padding: 0; box-sizing: border-box; }
  html, body {
    width: 1200px;
    height: 1200px;
    overflow: hidden;
    background: var(--stage);
    font-family: "Questrial", "Century Gothic", sans-serif;
  }
  .canvas {
    position: relative;
    width: 1200px;
    height: 1200px;
  }
  .card {
    position: absolute;
    left: 160px;
    width: 880px;
    height: 503px;
    overflow: hidden;
    box-shadow: 0 6px 18px rgba(0,0,0,0.18);
  }
  /* Front */
  .card--front {
    top: 60px;
    background: radial-gradient(ellipse at 45% 40%, var(--card-white) 45%, var(--card-grey) 100%);
  }
  .brand {
    position: absolute;
    left: 96px;
    top: 150px;
    display: flex;
    align-items: center;
    gap: 22px;
  }
  .brand__square {
    width: 96px;
    height: 96px;
    background: var(--brand-blue);
    border-radius: 10px;
  }
  .brand__name {
    color: var(--brand-blue);
    font-size: 60px;
    line-height: 0.95;
    text-transform: uppercase;
    letter-spacing: 1px;
  }
  .holder {
    position: absolute;
    left: 96px;
    top: 300px;
  }
  .holder__name {
    color: var(--brand-blue);
    font-size: 40px;
    font-weight: 700;
    line-height: 1;
  }
  .holder__role {
    color: var(--ink);
    font-size: 13px;
    margin-top: 4px;
    white-space: nowrap;
  }
  .contact {
    position: absolute;
    display: flex;
    align-items: center;
    gap: 8px;
    color: var(--ink);
    font-size: 17px;
    white-space: nowrap;
  }
  .contact svg { width: 18px; height: 18px; flex: none; }
  .contact--phone { left: 500px; top: 316px; }
  .contact--web { left: 680px; top: 316px; }
  .contact--email { left: 96px; top: 384px; }
  .front-band {
    position: absolute;
    left: 0;
    right: 0;
    bottom: 0;
    height: 80px;
    background: var(--brand-blue);
  }
  /* Back */
  .card--back {
    top: 637px;
  }
  .back-pattern {
    position: absolute;
    inset: 0;
    background: linear-gradient(135deg, var(--pattern-light) 0%, var(--brand-blue) 55%, var(--brand-blue-dark) 100%);
  }
  .back-brand {
    position: absolute;
    inset: 0;
    display: flex;
    align-items: center;
    justify-content: center;
    color: var(--card-white);
    font-size: 48px;
    text-transform: uppercase;
    letter-spacing: 2px;
  }
</style>
</head>
<body>
<main class="canvas">
  <section class="card card--front" aria-label="Business card front">
    <div class="brand">
      <div class="brand__square"></div>
      <div class="brand__name">Halvex<br>Consulting</div>
    </div>

    <div class="holder">
      <div class="holder__name">Gareth Pollard</div>
      <div class="holder__role">Unified Communications and Network Architect / Design Engineer</div>
    </div>

    <div class="contact contact--phone">
      <svg viewBox="0 0 24 24" aria-hidden="true"><path d="M6.6 10.8a15 15 0 0 0 6.6 6.6l2.2-2.2c.3-.3.7-.4 1-.2 1.1.4 2.3.6 3.6.6.6 0 1 .4 1 1V20c0 .6-.4 1-1 1A17 17 0 0 1 3 4c0-.6.4-1 1-1h3.5c.6 0 1 .4 1 1 0 1.3.2 2.5.6 3.6.1.3 0 .7-.2 1z" fill="#222"/></svg>
      <span>+64 9 555 0142</span>
    </div>
    <div class="contact contact--web">
      <svg viewBox="0 0 24 24" aria-hidden="true" fill="none" stroke="#222" stroke-width="1.6"><circle cx="12" cy="12" r="9"/><ellipse cx="12" cy="12" rx="4" ry="9"/><path d="M3 12h18M4.5 7.5h15M4.5 16.5h15"/></svg>
      <span>www.halvex.co.nz</span>
    </div>
    <div class="contact contact--email">
      <svg viewBox="0 0 24 24" aria-hidden="true" fill="none" stroke="#222" stroke-width="1.6"><rect x="3" y="6" width="18" height="12"/><path d="M3 6l9 7 9-7"/></svg>
      <span>gareth@halvex.co.nz</span>
    </div>

    <div class="front-band"></div>
  </section>

  <section class="card card--back" aria-label="Business card back">
    <div class="back-pattern" role="img" aria-label="Repeating pattern of linked rounded node shapes in lighter blue"></div>
    <div class="back-brand">Halvex Consulting</div>
  </section>
</main>
</body>
</html>
```